Business card for massage therapy company called Brook Fern Wellness

Need business card for massage therapy company called Brook Fern Wellness. Would like my logo on the front and the back of the card I have 3 options of logos and you can play with what looks better.

Would like this information displayed on the back of the card:

Marcus Ellery
Licensed Massage Therapist
321-555-0147
brookfern-example.com
brookfern_rest_

```html
<!DOCTYPE html>
<html lang="en">
<head>
<meta charset="utf-8">
<title>Brook Fern Wellness – Business Card</title>
<link rel="stylesheet" href="https://fonts.googleapis.com/css2?family=Marcellus&display=swap">
<style>
  :root {
    --backdrop: #e6e3dd;
    --sage: #6e775e;
    --paper: #f3f2ee;
    --clay: #b5896c;
    --clay-light: #c89c80;
    --clay-dark: #a97b5f;
    --ink-light: #f1f0ea;
    --card-w: 540px;
    --card-h: 309px;
  }
  * { box-sizing: border-box; margin: 0; padding: 0; }
  html, body {
    width: 1200px; height: 787px; overflow: hidden;
    background: var(--backdrop);
    font-family: "Marcellus", "Optima", serif;
  }
  .canvas {
    width: 1200px; height: 787px;
    display: flex; align-items: center; justify-content: center; gap: 40px;
  }
  .card {
    position: relative;
    width: var(--card-w); height: var(--card-h);
    border-radius: 18px; overflow: hidden;
    box-shadow: 0 6px 18px rgba(0,0,0,.12);
  }
  .card svg.card-shapes { position: absolute; inset: 0; }

  /* Front */
  .card-front { background: var(--paper); }
  .technique-emblem {
    position: absolute; left: 62px; top: 26px; width: 176px; height: 176px;
    border-radius: 10px;
    background: linear-gradient(160deg, var(--clay-light), var(--clay-dark));
  }
  .brand-name {
    position: absolute; right: 46px; top: 172px;
    color: var(--sage); text-align: right;
    font-size: 34px; line-height: 1.05; letter-spacing: .5px;
  }

  /* Back */
  .card-back { background: var(--sage); color: var(--ink-light); }
  .therapist { position: absolute; left: 34px; top: 32px; }
  .therapist .name { font-size: 26px; letter-spacing: .4px; }
  .therapist .role { font-size: 14px; letter-spacing: .4px; margin-top: 2px; }
  .rule { display: block; width: 16px; height: 2px; background: var(--ink-light); margin-top: 6px; }
  .contact { position: absolute; left: 34px; top: 140px; font-size: 14px; line-height: 1.55; }
  .contact li { list-style: none; display: flex; align-items: center; gap: 8px; }
  .contact .location-rule { margin: 0 0 4px; }
  .contact svg { width: 13px; height: 13px; flex: none; }
  .back-mark {
    position: absolute; left: 372px; top: 196px; width: 150px;
    text-align: center;
    color: var(--sage); font-size: 18px; line-height: 1.2; letter-spacing: .5px;
  }
</style>
</head>
<body>
<main class="canvas">

  <section class="card card-front" aria-label="Card front">
    <svg class="card-shapes" viewBox="0 0 540 309" aria-hidden="true">
      <circle cx="150" cy="100" r="162" fill="none" stroke="var(--sage)" stroke-width="1.6"/>
      <circle cx="148" cy="94" r="150" fill="var(--clay)"/>
      <path d="M270 20 A150 150 0 0 1 268 200" fill="none" stroke="var(--clay)" stroke-width="1.2"/>
    </svg>
    <div class="technique-emblem" role="img" aria-label="Barefoot massage emblem: therapist balancing on overhead bars above a client on a table, with the technique name below"></div>
    <div class="brand-name">Brook Fern<br>Wellness</div>
  </section>

  <section class="card card-back" aria-label="Card back">
    <svg class="card-shapes" viewBox="0 0 540 309" aria-hidden="true">
      <circle cx="470" cy="250" r="150" fill="none" stroke="var(--ink-light)" stroke-width="1.2" opacity=".8"/>
      <circle cx="480" cy="258" r="158" fill="none" stroke="var(--ink-light)" stroke-width="1" opacity=".6"/>
      <circle cx="478" cy="262" r="138" fill="var(--paper)"/>
    </svg>

    <div class="therapist">
      <div class="name">Marcus Ellery</div>
      <div class="role">Licensed Massage Therapist</div>
      <span class="rule"></span>
    </div>

    <ul class="contact">
      <li>Fern Hollow, Florida</li>
      <li><span class="rule location-rule"></span></li>
      <li>
        <svg viewBox="0 0 16 16" aria-hidden="true"><path d="M4 1.5l2.5 3-1.6 1.8a9 9 0 0 0 4.8 4.8l1.8-1.6 3 2.5-1.8 2.2C7.5 14 2 8.5 1.8 3.3z" fill="var(--ink-light)"/></svg>
        321-555-0147
      </li>
      <li>
        <svg viewBox="0 0 16 16" aria-hidden="true"><circle cx="8" cy="8" r="6.5" fill="none" stroke="var(--ink-light)" stroke-width="1.4"/><path d="M1.5 8h13M8 1.5c-3 3.5-3 9.5 0 13M8 1.5c3 3.5 3 9.5 0 13" fill="none" stroke="var(--ink-light)" stroke-width="1.1"/></svg>
        brookfern-example.com
      </li>
      <li>
        <svg viewBox="0 0 16 16" aria-hidden="true"><rect x="2" y="2" width="12" height="12" rx="1" fill="none" stroke="var(--ink-light)" stroke-width="1.5"/></svg>
        brookfern_rest_
      </li>
    </ul>

    <div class="back-mark">Brook Fern<br>Wellness</div>
  </section>

</main>
</body>
</html>
```